Architecture firm needing a business card

We need a business card design for a new company based in the US called "Pellmore Architecture". Seeking minimalist designs that have a creativity/design feel but must be clean and professional. Please refer to the logo attached.

Target Market(s)

Real Estate Investors, Home Builders and Construction Firms.

Industry/Entity Type

Architecture

Contact Information for Business Card

Standard US size business cards. Would like to have some sort of graphic on the back side of the card - nothing that is too loud but something that may catch your attention. More or less grayscale colors that are in line with the logo colors (navy and greys essentially). Additional colors maybe accepted if blended properly (earthtones), but might be difficult to accomplish and maintain the clean/minimalist look.

Requirements
Must have
• Clean Lines
Nice to have
• some sort of graphics, would like to have something creative on the back side of the card
Should not have
• nothing too busy, cluttered or overwhelming.

```html
<!DOCTYPE html>
<html lang="en">
<head>
<meta charset="utf-8">
<title>Pellmore Architecture – Business Card</title>
<link rel="stylesheet" href="https://fonts.googleapis.com/css2?family=Open+Sans:wght@400;600&display=swap">
<style>
  :root {
    --stage: #1b1b1c;
    --paper: #f4f5f6;
    --navy: #1f4f85;
    --navy-deep: #1a4676;
    --navy-light: #3a6a9c;
    --ink: #24466f;
    --silver: #d9dde2;
    --white: #ffffff;
  }
  * { box-sizing: border-box; margin: 0; padding: 0; }
  html, body {
    width: 1200px; height: 864px; overflow: hidden;
    background: var(--stage);
    font-family: "Open Sans", Arial, sans-serif;
  }
  .stage {
    position: relative; width: 1200px; height: 864px;
    display: flex; align-items: center; justify-content: center; gap: 60px;
  }
  .card {
    position: relative; width: 500px; height: 286px;
    overflow: hidden; border-radius: 2px;
    box-shadow: 0 14px 30px rgba(0,0,0,.55);
  }

  /* Front */
  .card-front { background: var(--paper); }
  .front-header {
    height: 44%; display: flex; align-items: center; justify-content: center;
  }
  .wordmark { text-align: center; color: var(--ink); font-weight: 600; line-height: 1; }
  .wordmark-name { font-size: 34px; letter-spacing: 1px; }
  .wordmark-sub { font-size: 13px; letter-spacing: 5px; margin-top: 5px; }
  .front-band {
    position: absolute; left: 0; right: 0; bottom: 0; height: 56%;
    background: linear-gradient(170deg, var(--navy-light), var(--navy) 60%, var(--navy-deep));
    display: flex; align-items: center; justify-content: center;
    color: var(--white);
  }
  .holder { text-align: right; padding-right: 22px; font-size: 11.5px; line-height: 1.45; }
  .holder-name { font-weight: 600; font-size: 13px; }
  .holder-title { font-weight: 600; margin-bottom: 8px; }
  .divider { width: 1px; height: 96px; background: rgba(255,255,255,.55); }
  .contacts { list-style: none; padding-left: 22px; font-size: 12px; }
  .contacts li { display: flex; align-items: center; gap: 9px; height: 21px; }
  .contacts svg { width: 12px; height: 12px; flex: none; }

  /* Back */
  .card-back {
    background: linear-gradient(160deg, var(--navy-deep), var(--navy) 55%, var(--navy-light));
    display: flex; align-items: center; justify-content: center;
  }
  .back-mark { display: flex; align-items: center; gap: 14px; color: var(--silver); font-weight: 600; }
  .back-square { width: 22px; height: 22px; background: var(--silver); }
  .back-name { font-size: 30px; letter-spacing: 1px; }
</style>
</head>
<body>
<main class="stage">
  <section class="card card-front" aria-label="Business card front">
    <div class="front-header">
      <div class="wordmark">
        <div class="wordmark-name">PELLMORE</div>
        <div class="wordmark-sub">ARCHITECTURE</div>
      </div>
    </div>
    <div class="front-band">
      <div class="holder">
        <p class="holder-name">Dana K. Whitfield</p>
        <p class="holder-title">Director</p>
        <p>412 Cedar Hollow Road</p>
        <p>Marlow, VA 22650</p>
      </div>
      <div class="divider"></div>
      <ul class="contacts">
        <li>
          <svg viewBox="0 0 12 12" aria-hidden="true"><path d="M3 1 L5 3.5 L4 4.8 Q5 7 7.2 8 L8.5 7 L11 9 L9.5 11 Q4.5 10.5 1 3 Z" fill="var(--white)"/></svg>
          (0000) 555 018
        </li>
        <li>
          <svg viewBox="0 0 12 12" aria-hidden="true"><rect x="1" y="2.5" width="10" height="7" fill="none" stroke="var(--white)" stroke-width="1.2"/><path d="M1 3 L6 7 L11 3" fill="none" stroke="var(--white)" stroke-width="1.2"/></svg>
          info@pellmorearch.com
        </li>
        <li>
          <svg viewBox="0 0 12 12" aria-hidden="true"><circle cx="6" cy="6" r="4.8" fill="none" stroke="var(--white)" stroke-width="1.1"/><ellipse cx="6" cy="6" rx="2" ry="4.8" fill="none" stroke="var(--white)" stroke-width="1"/><path d="M1.2 6 H10.8" stroke="var(--white)" stroke-width="1"/></svg>
          www.pellmorearch.com
        </li>
      </ul>
    </div>
  </section>

  <section class="card card-back" aria-label="Business card back">
    <div class="back-mark">
      <span class="back-square"></span>
      <span class="back-name">PELLMORE</span>
    </div>
  </section>
</main>
</body>
</html>
```